Web design for a dental and eye clinic

We need a web design for a dental and eye clinic ( with medical laboratory services) with two branches in Lagos Nigeria. The ultimate aim is to attract more patronage. The design should have links to social media and should have provision for appointments and enquiries. Blue should be part of the colours

Name of facility. VORANTACARE Added Saturday, May 27, 2017

Target Market(s)

Lagos. Nigeria

Industry/Entity Type

Health Care

Number of Pages Required

3 page

Font styles to use
Sans Serif

Colors
85cae6
cadf82

Requirements
Must have
• a projection of the professioal services rendered
Nice to have
• portal for enquiries and appointments
• Link to our facebook, twitter and instagram

```html
<!DOCTYPE html>
<html lang="en">
<head>
<meta charset="utf-8">
<title>Vorantacare — Dental &amp; Eye Clinic</title>
<link href="https://fonts.googleapis.com/css2?family=Lato:wght@400;700&family=Open+Sans:wght@400;600;700&family=PT+Serif:wght@700&display=swap" rel="stylesheet">
<style>
:root{
  --sky:#85cae6;
  --lime:#cadf82;
  --lime-dark:#b9d16a;
  --blue:#2aa8e0;
  --ink:#2d2d2d;
  --grey:#777;
  --light:#f3f3f3;
  --footer:#2b2b2b;
  --footer-deep:#1e1e1e;
  --white:#fff;
}
*{box-sizing:border-box;margin:0;padding:0}
html,body{width:1200px;height:3175px;overflow:hidden}
body{position:relative;background:var(--white);font-family:'Lato',sans-serif;color:var(--ink)}
section,header,nav,footer,.topbar{position:absolute;left:0;width:1200px}
a{color:inherit;text-decoration:none}

/* top bar */
.topbar{top:0;height:52px;background:var(--sky);display:flex;align-items:center;justify-content:space-between;padding:0 40px;color:var(--white);font-size:13px}
.login{display:flex;align-items:center;gap:10px}
.socials{display:flex;gap:14px}
.social{width:14px;height:14px;border-radius:50%;background:var(--white);opacity:.9}

/* header */
.site-header{top:52px;height:160px;display:flex;align-items:center;justify-content:space-between;padding:0 40px 0 40px}
.brand{display:flex;align-items:center;gap:12px;font-family:'Open Sans',sans-serif;font-weight:700;font-size:34px;color:var(--blue)}
.brand-dot{width:40px;height:40px;border-radius:50%;background:var(--sky)}
.contacts{display:flex;gap:40px;margin-right:4px}
.contact{display:flex;align-items:center;gap:22px}
.contact-ring{width:76px;height:76px;border-radius:50%;border:2px solid var(--sky);display:flex;align-items:center;justify-content:center}
.contact-text{font-size:17px;color:var(--grey);line-height:1.5}
.contact-text b{color:#555;font-weight:400}

/* nav */
.main-nav{top:212px;height:53px;background:var(--lime);display:flex;align-items:center;padding-left:40px}
.main-nav ul{display:flex;list-style:none;gap:57px;font-family:'Open Sans',sans-serif;font-size:16.5px;color:var(--white);font-weight:600}
.appointment-tab{position:absolute;right:0;top:0;height:53px;width:284px;background:var(--lime-dark);display:flex;align-items:center;justify-content:center;gap:26px;color:var(--white);font-family:'Open Sans',sans-serif;font-weight:700;font-size:19px}

/* hero */
.hero{top:265px;height:416px;background:linear-gradient(100deg,#8fa4b3 0%,#c8b5a8 35%,#d9d6d4 60%,#9aa6ae 100%);overflow:hidden}
.hero-title{position:absolute;left:38px;top:98px;font-family:'Open Sans',sans-serif;font-size:56px;line-height:1.16;color:var(--white);font-weight:400}
.btn-blue{display:inline-block;background:var(--blue);color:var(--white);font-family:'Open Sans',sans-serif;font-weight:600}
.hero .btn-blue{position:absolute;left:40px;top:260px;width:178px;height:46px;line-height:46px;text-align:center;font-size:22px}
.dots{position:absolute;left:568px;top:385px;display:flex;gap:16px}
.dots i{width:8px;height:8px;border-radius:50%;background:rgba(255,255,255,.6)}
.dots i.on{background:var(--white)}

/* intro */
.intro{top:681px;height:525px}
.intro h2{position:absolute;left:42px;top:50px;font-family:'Open Sans',sans-serif;font-size:29px;font-weight:700}
.intro .lead{position:absolute;left:40px;top:112px;width:720px;font-size:18px;line-height:1.5;color:var(--blue)}
.intro .body{position:absolute;left:40px;top:188px;width:740px;font-size:16.5px;line-height:1.6;color:var(--grey)}
.features{position:absolute;left:40px;top:320px;display:flex;gap:43px}
.feature{width:195px}
.feature h3{margin-top:18px;font-family:'Open Sans',sans-serif;font-size:17px;font-weight:700}
.feature p{margin-top:12px;font-size:13px;line-height:1.4;color:var(--grey);width:175px}
.appt-form{position:absolute;left:808px;top:60px;width:348px;height:408px;border:5px solid #eee;padding:26px 28px}
.appt-form h4{font-family:'Open Sans',sans-serif;font-size:14px;font-weight:700;margin-bottom:20px}
.field{border:1px solid #e3e3e3;height:34px;font-size:11px;color:#aaa;padding:9px 12px;margin-bottom:16px}
.row{display:flex;gap:20px}.row .field{flex:1}
.field.tall{height:86px}
.submit{display:inline-block;margin-top:6px;background:var(--blue);color:var(--white);font-size:10px;font-weight:700;padding:11px 18px;letter-spacing:.5px}

/* services */
.services{top:1206px;height:519px;background:linear-gradient(180deg,#eef1f3 0%,#f6f6f6 50%,#eceff1 100%);text-align:center}
.section-title{font-family:'Open Sans',sans-serif;font-size:30px;font-weight:700;padding-top:40px}
.section-sub{margin-top:10px;font-size:15px;color:#aaa}
.tabs{margin-top:36px;display:flex;justify-content:center;gap:40px;font-family:'Open Sans',sans-serif;font-size:16px;color:var(--grey)}
.tabs span{padding:4px 22px}
.tabs .active{background:var(--lime);color:var(--white)}
.service-list{margin-top:46px;display:flex;justify-content:center;gap:96px}
.service{width:140px}
.service-icon{width:125px;height:125px;border-radius:50%;background:var(--blue);margin:0 auto;display:flex;align-items:center;justify-content:center}
.service h3{margin-top:28px;font-size:12.5px;color:var(--blue);font-weight:400;white-space:nowrap}
.service p{margin-top:10px;font-size:12.5px;line-height:1.55;color:#666;width:170px;margin-left:-15px}

/* team */
.team{top:1725px;height:582px;text-align:center}
.team .section-title{padding-top:48px}
.arrows{position:absolute;right:46px;top:100px;display:flex;border:2px solid var(--ink)}
.arrows span{width:49px;height:46px;display:flex;align-items:center;justify-content:center}
.arrows span+span{border-left:2px solid var(--ink)}
.team-cards{position:absolute;left:44px;top:193px;display:flex;gap:28px}
.member{width:256px;height:332px;background:linear-gradient(180deg,#eef2f4,#cdd6dc)}
.member.featured{position:relative;background:var(--sky);color:var(--white);padding-top:84px}
.member.featured::after{content:"";position:absolute;right:0;top:0;border-style:solid;border-width:0 46px 46px 0;border-color:transparent #3a3a3a transparent transparent}
.member h3{font-family:'Open Sans',sans-serif;font-size:17px;font-weight:700;letter-spacing:.5px}
.member .role{margin-top:10px;font-size:13px;font-weight:700}
.member .links{margin:16px auto 0;display:flex;justify-content:center;gap:18px}
.member .links i{width:9px;height:9px;border-radius:50%;background:rgba(255,255,255,.6)}
.member .quote{margin-top:22px;font-size:13px;line-height:1.6}

/* blog */
.blog{top:2307px;height:520px;background:var(--light);text-align:center}
.blog .section-title{padding-top:36px}
.posts{position:absolute;left:92px;top:152px;display:flex;gap:24px;text-align:left}
.post{width:323px}
.post-image{height:172px}
.post-meta{margin-top:24px;font-size:11px;color:#999}
.post h3{margin-top:10px;width:295px;font-family:'PT Serif',serif;font-size:20px;line-height:1.4;color:var(--ink)}
.read-more{display:inline-block;margin-top:20px;background:#333;color:var(--white);font-size:11px;padding:10px 22px}

/* footer */
.site-footer{top:2827px;height:348px;background:var(--footer);color:#ddd}
.footer-cols{position:absolute;left:40px;top:40px;display:flex}
.footer-cols h4{font-family:'Open Sans',sans-serif;font-size:15px;font-weight:600;color:var(--white);margin-bottom:30px}
.col-contacts{width:370px}
.col-links{width:212px}
.col-news{width:313px}
.addr{display:flex;gap:18px;font-size:12.5px;line-height:1.7;margin-bottom:24px}
.addr svg{flex:none;margin-top:4px}
.col-links ul{list-style:none;font-size:12px;line-height:2.25}
.col-news p{font-size:12px;line-height:1.7;width:230px}
.email-box{margin-top:20px;width:226px;height:36px;background:var(--white);color:#333;font-size:12px;padding:10px}
.subscribe{margin-top:22px;width:226px;height:36px;background:#4a90d2;color:var(--white);font-size:12px;text-align:center;line-height:36px}
.map{width:226px;height:152px;background:linear-gradient(135deg,#e7e4dc,#d9e4ec 60%,#e9e2d2)}
.footer-bottom{position:absolute;left:0;bottom:0;width:1200px;height:56px;background:var(--footer-deep);display:flex;align-items:center;justify-content:space-between;padding:0 40px;font-size:12px}
.footer-bottom .social{background:#4a90d2}
</style>
</head>
<body>

<div class="topbar">
  <div class="login">
    <svg width="16" height="18" viewBox="0 0 16 18"><circle cx="8" cy="5" r="4" fill="#fff"/><path d="M0 18c0-5 3.5-7 8-7s8 2 8 7z" fill="#fff"/></svg>
    <span>Log In</span>
  </div>
  <div class="socials" aria-label="Social links">
    <span class="social" role="img" aria-label="Social link 1"></span>
    <span class="social" role="img" aria-label="Social link 2"></span>
    <span class="social" role="img" aria-label="Social link 3"></span>
    <span class="social" role="img" aria-label="Social link 4"></span>
    <span class="social" role="img" aria-label="Social link 5"></span>
    <span class="social" role="img" aria-label="Social link 6"></span>
  </div>
</div>

<header class="site-header">
  <div class="brand"><span class="brand-dot"></span>Vorantacare</div>
  <div class="contacts">
    <div class="contact">
      <span class="contact-ring"><svg width="30" height="30" viewBox="0 0 24 24"><path d="M6.6 10.8a15 15 0 0 0 6.6 6.6l2.2-2.2c.3-.3.7-.4 1-.2 1.1.4 2.3.6 3.6.6.6 0 1 .4 1 1V20c0 .6-.4 1-1 1A17 17 0 0 1 3 4c0-.6.4-1 1-1h3.5c.6 0 1 .4 1 1 0 1.3.2 2.5.6 3.6.1.3 0 .7-.2 1z" fill="none" stroke="#85cae6" stroke-width="1.6"/></svg></span>
      <div class="contact-text">Call us :<br><b>+234 80 000 12 345</b></div>
    </div>
    <div class="contact">
      <span class="contact-ring"><svg width="32" height="24" viewBox="0 0 32 24"><rect x="1" y="1" width="30" height="22" fill="#85cae6"/><path d="M1 1l15 12L31 1" fill="none" stroke="#fff" stroke-width="2"/></svg></span>
      <div class="contact-text">Email :<br><b>info@vorantacare.com</b></div>
    </div>
  </div>
</header>

<nav class="main-nav">
  <ul>
    <li>HOME</li><li>ABOUT US</li><li>SERVICES</li><li>DOCTORS</li><li>BOLG</li><li>CONTACT US</li>
  </ul>
  <div class="appointment-tab">
    <svg width="28" height="28" viewBox="0 0 28 28"><rect x="2" y="4" width="24" height="22" fill="none" stroke="#fff" stroke-width="2"/><line x1="2" y1="10" x2="26" y2="10" stroke="#fff" stroke-width="2"/><line x1="8" y1="1" x2="8" y2="6" stroke="#fff" stroke-width="2"/><line x1="20" y1="1" x2="20" y2="6" stroke="#fff" stroke-width="2"/><g fill="#fff"><rect x="6" y="13" width="4" height="3"/><rect x="12" y="13" width="4" height="3"/><rect x="18" y="13" width="4" height="3"/><rect x="6" y="19" width="4" height="3"/><rect x="12" y="19" width="4" height="3"/><rect x="18" y="19" width="4" height="3"/></g></svg>
    APPOINTMENT
  </div>
</nav>

<section class="hero" role="img" aria-label="Dentist examining a smiling child's teeth beside an eye examination at a slit lamp">
  <h1 class="hero-title">Lorem ipsum dolor<br>sit ametconsec</h1>
  <a class="btn-blue">Learn More</a>
  <div class="dots"><i></i><i class="on"></i><i></i></div>
</section>

<section class="intro">
  <h2>The Best For Your Tretmet Eye and Dental !</h2>
  <p class="lead">Lorem ipsum dolor sit amet consectetur adipisicing elit Perferendis repudiandae nostrum quibusdam! elit Perferendis repudiandae</p>
  <p class="body">Lorem ipsum dolor sit amet, consectetur adipisicing elit. Ipsam, corrupti, fugit. Temporibus nostrum nam deleniti vitae accusantium iste sunt facilis, quisquam eveniet reiciendis corporis, veniam nulla. Provident tempora perspiciatis quod commodi iure neque eaque quos,</p>
  <div class="features">
    <div class="feature">
      <svg width="40" height="50" viewBox="0 0 40 50"><path d="M10 3c-6 0-9 5-8 12 1 6 4 10 5 18 1 7 3 14 6 14 4 0 3-12 7-12s3 12 7 12c3 0 5-7 6-14 1-8 4-12 5-18 1-7-2-12-8-12-4 0-6 2-10 2S14 3 10 3z" fill="none" stroke="#85cae6" stroke-width="2"/></svg>
      <h3>DENTAL DOCTOR</h3>
      <p>Aliquam erat volutpat Phase llus a purus</p>
    </div>
    <div class="feature">
      <svg width="64" height="50" viewBox="0 0 64 50"><path d="M2 25C14 10 50 10 62 25 50 40 14 40 2 25z" fill="none" stroke="#85cae6" stroke-width="2.5"/><circle cx="32" cy="25" r="9" fill="none" stroke="#85cae6" stroke-width="2.5"/><circle cx="32" cy="25" r="4" fill="#85cae6"/></svg>
      <h3>DENTAL DOCTOR</h3>
      <p>Aliquam erat volutpat Phase llus a purus</p>
    </div>
    <div class="feature">
      <svg width="40" height="50" viewBox="0 0 40 50"><rect x="16" y="4" width="8" height="20" transform="rotate(-25 20 14)" fill="none" stroke="#85cae6" stroke-width="2"/><path d="M8 44h26M12 44c-4-6-2-16 8-18" fill="none" stroke="#85cae6" stroke-width="2"/><rect x="18" y="38" width="12" height="6" fill="none" stroke="#85cae6" stroke-width="2"/></svg>
      <h3>DENTAL DOCTOR</h3>
      <p>Aliquam erat volutpat Phase llus a purus</p>
    </div>
  </div>
  <form class="appt-form">
    <h4>Appointment Form</h4>
    <div class="field">Your Name</div>
    <div class="row"><div class="field">Email</div><div class="field">Phone</div></div>
    <div class="row"><div class="field">Day</div><div class="field">time</div></div>
    <div class="field tall">Your Message...</div>
    <span class="submit">➜ SUBMIT</span>
  </form>
</section>

<section class="services" aria-label="Our services">
  <h2 class="section-title">OUR SERVICES</h2>
  <p class="section-sub">Ut enim ad minim veniam aliquip ex ea commodo consequat consectetuer adipiscing elit.</p>
  <div class="tabs"><span class="active">Dental</span><span>Eye</span><span>Medical Laboratory</span></div>
  <div class="service-list">
    <div class="service">
      <div class="service-icon"><svg width="60" height="60" viewBox="0 0 60 60" fill="none" stroke="#fff" stroke-width="3"><path d="M8 20l10 22h26l6 8"/><path d="M20 42l6-14h18"/><rect x="34" y="8" width="12" height="10"/></svg></div>
      <h3>SEDATION DENTISTRY</h3>
      <p>Lorem ipsum dolor sit amet conse ctetur elit, sed. Lorem ipsum dolor.</p>
    </div>
    <div class="service">
      <div class="service-icon"><svg width="60" height="60" viewBox="0 0 60 60" fill="none" stroke="#fff" stroke-width="3"><rect x="6" y="6" width="48" height="48"/><path d="M20 12c-6 0-8 6-6 14 2 6 2 20 6 20s3-10 10-10 6 10 10 10 4-14 6-20c2-8 0-14-6-14-4 0-6 2-10 2s-6-2-10-2z"/></svg></div>
      <h3>SEDATION DENTISTRY</h3>
      <p>Lorem ipsum dolor sit amet conse ctetur elit, sed. Lorem ipsum dolor.</p>
    </div>
    <div class="service">
      <div class="service-icon"><svg width="60" height="64" viewBox="0 0 60 64" fill="none" stroke="#fff" stroke-width="3"><path d="M14 8c6-4 12 0 16 0s10-4 16 0c6 6 2 16 0 20H14c-2-4-6-14 0-20z"/><path d="M16 28c2 10 2 30 8 30 4 0 2-16 6-16s2 16 6 16c6 0 6-20 8-30"/></svg></div>
      <h3>SEDATION DENTISTRY</h3>
      <p>Lorem ipsum dolor sit amet conse ctetur elit, sed. Lorem ipsum dolor.</p>
    </div>
    <div class="service">
      <div class="service-icon"><svg width="50" height="66" viewBox="0 0 50 66" fill="none" stroke="#fff" stroke-width="3"><path d="M8 6c6-4 12 0 17 0s11-4 17 0c3 4 2 10 0 14H8C6 16 5 10 8 6z"/><path d="M12 28h26M14 36h22M16 44h18M18 52h14M22 60h6"/></svg></div>
      <h3>SEDATION DENTISTRY</h3>
      <p>Lorem ipsum dolor sit amet conse ctetur elit, sed. Lorem ipsum dolor.</p>
    </div>
    <div class="service">
      <div class="service-icon"><svg width="60" height="60" viewBox="0 0 60 60" fill="none" stroke="#fff" stroke-width="3"><circle cx="40" cy="16" r="10"/><path d="M33 23L18 56"/><path d="M14 6v24l-6 26M14 30l6 26"/></svg></div>
      <h3>SEDATION DENTISTRY</h3>
      <p>Lorem ipsum dolor sit amet conse ctetur elit, sed. Lorem ipsum dolor.</p>
    </div>
  </div>
</section>

<section class="team" aria-label="Our experienced team">
  <h2 class="section-title">OUR EXPERIENCED TEAM</h2>
  <p class="section-sub">Ut enim ad minim veniam aliquip ex ea commodo consequat consectetuer adipiscing elit.</p>
  <div class="arrows">
    <span><svg width="18" height="10" viewBox="0 0 18 10"><path d="M18 5H2M6 1L2 5l4 4" fill="none" stroke="#2d2d2d" stroke-width="2"/></svg></span>
    <span><svg width="18" height="10" viewBox="0 0 18 10"><path d="M0 5h16M12 1l4 4-4 4" fill="none" stroke="#2d2d2d" stroke-width="2"/></svg></span>
  </div>
  <div class="team-cards">
    <div class="member" role="img" aria-label="Portrait of a doctor in a white coat holding a blue folder"></div>
    <div class="member featured">
      <h3>ADAEZE OKAFOR</h3>
      <p class="role">Co Founder / Dentist</p>
      <div class="links"><i></i><i></i><i></i><i></i></div>
      <p class="quote">We finally got a piece of the pie!<br>Why do we always come here</p>
    </div>
    <div class="member" role="img" aria-label="Portrait of a smiling doctor with a stethoscope"></div>
    <div class="member" role="img" aria-label="Portrait of a bearded doctor in a white coat"></div>
  </div>
</section>

<section class="blog" aria-label="Blog">
  <h2 class="section-title">BLOG</h2>
  <p class="section-sub">Ut enim ad minim veniam aliquip ex ea commodo consequat consectetuer adipiscing elit.</p>
  <div class="posts">
    <article class="post">
      <div class="post-image" role="img" aria-label="Surgeons operating in a theatre" style="background:linear-gradient(135deg,#9fd0dc,#4f9fb5)"></div>
      <p class="post-meta">Oct 19th, 2016 · 10 Comments · by Authore</p>
      <h3>What is the success rate of a Root Canel?</h3>
      <a class="read-more">Read more</a>
    </article>
    <article class="post">
      <div class="post-image" role="img" aria-label="Dental surgeon wearing a mask and cap" style="background:linear-gradient(135deg,#cfe6ee,#5d9fc0)"></div>
      <p class="post-meta">Oct 19th, 2016 · 10 Comments · by Authore</p>
      <h3>Cosmetic Dentistry Techniques Explained</h3>
      <a class="read-more">Read more</a>
    </article>
    <article class="post">
      <div class="post-image" role="img" aria-label="Doctor touching a screen of medical icons" style="background:linear-gradient(135deg,#e8f2fa,#3c8fd0)"></div>
      <p class="post-meta">Oct 19th, 2016 · 10 Comments · by Authore</p>
      <h3>Synthetic Glycopolymer Tests Mucoadhesion</h3>
      <a class="read-more">Read more</a>
    </article>
  </div>
</section>

<footer class="site-footer">
  <div class="footer-cols">
    <div class="col-contacts">
      <h4>CONTACTS</h4>
      <div class="addr"><svg width="12" height="16" viewBox="0 0 12 16"><path d="M6 0a6 6 0 0 0-6 6c0 4 6 10 6 10s6-6 6-10a6 6 0 0 0-6-6z" fill="#ddd"/><circle cx="6" cy="6" r="2" fill="#2b2b2b"/></svg><span>7 Harbour Lane, Palm Grove Estate, Km 18<br>Coastal Road, Lekki. 22, Orchid Avenue,<br>G.R.A, Ikeja Lagos.</span></div>
      <div class="addr"><svg width="14" height="14" viewBox="0 0 24 24"><path d="M6.6 10.8a15 15 0 0 0 6.6 6.6l2.2-2.2c.3-.3.7-.4 1-.2 1.1.4 2.3.6 3.6.6.6 0 1 .4 1 1V20c0 .6-.4 1-1 1A17 17 0 0 1 3 4c0-.6.4-1 1-1h3.5c.6 0 1 .4 1 1 0 1.3.2 2.5.6 3.6.1.3 0 .7-.2 1z" fill="#ddd"/></svg><span>+234 80 000 12 345</span></div>
      <div class="addr"><svg width="14" height="11" viewBox="0 0 14 11"><rect width="14" height="11" fill="#ddd"/><path d="M0 0l7 6 7-6" fill="none" stroke="#2b2b2b" stroke-width="1.4"/></svg><span>info@vorantacare.com</span></div>
    </div>
    <div class="col-links">
      <h4>QUICK LINKS</h4>
      <ul><li>HOME</li><li>ABOUT US</li><li>SERVICES</li><li>DOCTORS</li><li>BOLG</li><li>CONTACT US</li></ul>
    </div>
    <div class="col-news">
      <h4>NEWSLETTER</h4>
      <p>Enter your e-mail and subscribe to our newsletter</p>
      <div class="email-box">E - mail</div>
      <div class="subscribe">SUBSCRIBE</div>
    </div>
    <div class="col-map">
      <h4>LOCATION</h4>
      <div class="map" role="img" aria-label="Street map showing the clinic location"></div>
    </div>
  </div>
  <div class="footer-bottom">
    <span>Copyright © . All Rights Reserved</span>
    <div class="socials">
      <span class="social" role="img" aria-label="Social link 1"></span>
      <span class="social" role="img" aria-label="Social link 2"></span>
      <span class="social" role="img" aria-label="Social link 3"></span>
      <span class="social" role="img" aria-label="Social link 4"></span>
      <span class="social" role="img" aria-label="Social link 5"></span>
      <span class="social" role="img" aria-label="Social link 6"></span>
    </div>
  </div>
</footer>

</body>
</html>
```